Travel Company is looking for a STAND OUT Business Card

I need a unique Business Card that will truly stand out. Nothing too busy. Simple is good, right? Not looking for a standard design either. No cookie cutter layout. We are a Travel Company that works more with Companies than Travelers. I had an idea to focus and emphasis on the 2 logo a bit more. This is not necessary, however thought it would look interesting. I am just looking for something interesting and a bit different. Does't have to completely off the wall crazy, just not your run of the mill business card.

Target Market(s)

Hoteliers, Resort Management, Call Centers, Executives, Travelers, Families, Businesses

Industry/Entity Type

Hospitality

Contact Information for Business Card

President/CEO - Marcus T Bellamy (title not necessary if design doesn't allow for it)
contact - (407) 555-0186
email - mbellamy@wayfarenow.example
address - 4812 Quillmore Ave #164
Orlando, FL 32804
website - www.wayfarenow.example

Font styles to use
Serif
Other font styles liked:
• Avenir Next LT Pro BOLD

Requirements
Must have
• simple look and design. Unique design
Nice to have
• I attached the 2 logo separate from the main logo. This can be used separately from the Main Logo, together with the main logo or as main logo. I included the logo font. Use it or not, designers choice.
Should not have
• cookie cutter design. Little use of red other than the logo

```html
<!DOCTYPE html>
<html lang="en">
<head>
<meta charset="utf-8">
<title>Wayfare Now – Business Card</title>
<link rel="stylesheet" href="https://fonts.googleapis.com/css2?family=Source+Sans+3:wght@400;600;700&display=swap">
<style>
  :root {
    --stage: #5a5a5a;
    --card-dark: #262626;
    --card-light: #ffffff;
    --ink-white: #ffffff;
    --ink-dark: #1c1c1c;
    --ink-grey: #6b6b6b;
    --accent-red: #e3141b;
    --divider: #9a9a9a;
  }
  * { margin: 0; padding: 0; box-sizing: border-box; }
  html, body {
    width: 1200px;
    height: 1000px;
    overflow: hidden;
  }
  body {
    background: var(--stage);
    font-family: "Source Sans 3", "Helvetica Neue", Arial, sans-serif;
    position: relative;
  }
  .card {
    position: absolute;
    left: 288px;
    width: 625px;
    height: 357px;
  }
  .card--front {
    top: 141px;
    background: var(--card-dark);
    display: flex;
    align-items: center;
    justify-content: center;
  }
  .card--back {
    top: 531px;
    height: 358px;
    background: var(--card-light);
  }
  .brand-name {
    font-weight: 700;
    font-size: 64px;
    letter-spacing: -1px;
    color: var(--ink-white);
    display: flex;
    align-items: center;
    gap: 16px;
    margin-top: -30px;
  }
  .brand-dot {
    width: 22px;
    height: 22px;
    border-radius: 50%;
    background: var(--accent-red);
  }
  .back-brand {
    position: absolute;
    left: 0;
    width: 312px;
    top: 0;
    height: 358px;
    display: flex;
    align-items: center;
    justify-content: center;
    padding-left: 30px;
  }
  .back-brand .brand-name {
    color: var(--ink-dark);
    font-size: 30px;
    letter-spacing: -0.5px;
    gap: 10px;
    margin-top: 0;
  }
  .back-brand .brand-dot {
    width: 14px;
    height: 14px;
  }
  .divider {
    position: absolute;
    left: 312px;
    top: 107px;
    width: 1px;
    height: 145px;
    background: var(--divider);
  }
  .contact {
    position: absolute;
    left: 337px;
    top: 105px;
    color: var(--ink-grey);
    font-size: 14px;
    line-height: 18px;
  }
  .contact__name {
    color: var(--accent-red);
    font-weight: 700;
    font-size: 18px;
    line-height: 22px;
  }
  .contact__title {
    margin-bottom: 13px;
  }
  .contact__row {
    display: flex;
    align-items: flex-start;
    gap: 6px;
  }
  .contact__row + .contact__row { margin-top: 0; }
  .contact__row--gap { margin-bottom: 4px; }
  .contact__icon {
    width: 11px;
    height: 11px;
    margin-top: 4px;
    flex: none;
    fill: var(--accent-red);
  }
</style>
</head>
<body>

<section class="card card--front">
  <div class="brand-name"><span>Wayfare Now</span><span class="brand-dot"></span></div>
</section>

<section class="card card--back">
  <div class="back-brand">
    <div class="brand-name"><span class="brand-dot"></span><span>Wayfare Now</span></div>
  </div>
  <div class="divider"></div>
  <div class="contact">
    <div class="contact__name">Marcus T Bellamy</div>
    <div class="contact__title">President/CEO</div>

    <div class="contact__row contact__row--gap">
      <svg class="contact__icon" viewBox="0 0 12 12" aria-hidden="true"><path d="M6 0a4 4 0 0 0-4 4c0 3 4 8 4 8s4-5 4-8a4 4 0 0 0-4-4zm0 5.6A1.6 1.6 0 1 1 6 2.4a1.6 1.6 0 0 1 0 3.2z"/></svg>
      <div>4812 Quillmore Ave #164<br>Orlando, FL 32804</div>
    </div>
    <div class="contact__row">
      <svg class="contact__icon" viewBox="0 0 12 12" aria-hidden="true"><path d="M2.4 0.5l2 2.3-1 1.4a7 7 0 0 0 4.4 4.4l1.4-1 2.3 2-1 1.9C5.6 11.8 0.2 6.4 0.5 1.5z"/></svg>
      <div>(407) 555-0186</div>
    </div>
    <div class="contact__row">
      <svg class="contact__icon" viewBox="0 0 12 12" aria-hidden="true"><path d="M0 2h12v1.2L6 7 0 3.2zM0 4.6l6 3.8 6-3.8V10H0z"/></svg>
      <div>mbellamy@wayfarenow.example</div>
    </div>
    <div class="contact__row">
      <svg class="contact__icon" viewBox="0 0 12 12" aria-hidden="true"><path d="M6 0a6 6 0 1 0 0 12A6 6 0 0 0 6 0zm4.7 5.3H8.6a9 9 0 0 0-.8-3.6 4.8 4.8 0 0 1 2.9 3.6zM6 1.2c.6.8 1.3 2.2 1.4 4.1H4.6C4.7 3.4 5.4 2 6 1.2zM4.2 1.7a9 9 0 0 0-.8 3.6H1.3a4.8 4.8 0 0 1 2.9-3.6zM1.3 6.7h2.1a9 9 0 0 0 .8 3.6 4.8 4.8 0 0 1-2.9-3.6zM6 10.8c-.6-.8-1.3-2.2-1.4-4.1h2.8c-.1 1.9-.8 3.3-1.4 4.1zm1.8-.5a9 9 0 0 0 .8-3.6h2.1a4.8 4.8 0 0 1-2.9 3.6z"/></svg>
      <div>www.wayfarenow.example</div>
    </div>
  </div>
</section>

</body>
</html>
```